Podcast covert art for startup show

I need podcast cover art that stands out and clearly says what the podcast is about: startup stories.

This is an example of Castrova cover art:
https://www.filebarnex.com/s/q4k8tmwpl2vbx9r/Castrova%202.png?dl=0

You can see how mine is looking blah on this page:
https://www.filebarnex.com/s/7h3jrdkqa5wzm2f/My%20podcast%20art%20doesn%27t%20stand%20out%20enough.png?dl=0

I need something that will get attention on a page that's full of other podcast covers and be easy to read.

SOMETHINGS THAT MIGHT HELP:

I love how easy it is to read the titles of these podcasts:
https://www.filebarnex.com/s/wpx6ghtmr0cqv84/easy%20to%20read%20titles.png?dl=0

I love how the logos of these podcasts are easy to read but they don't take much space:
https://www.filebarnex.com/s/5t2yfnbkd8jxe63/nice%20logo%20placement.png?dl=0

Target Market(s)

Successful software entrepreneurs

Industry/Entity Type

Startup

Font styles to use
Serif

Colors
00a990

Requirements
Must have
• I need it to include this:
• - This phrase: Startup Stories
• - My logo (keep it small, but readable)
• - My photo
• MY LOGO:
• http://talvoren.com/logo
• MY FAVORITE PHOTO OF MYSELF:
• https://vault.stormlake.net/open?id=0Xq7T_pwkr5bnHYmQZAaLPKKRw3
• You can edit my photo any way you want, including removing the background, turning me into a black&white photo, etc
• OTHER PHOTOS OF ME:
• https://vault.stormlake.net/open?id=0Xq7T_pwkr5bnW8JdvqXAcMbPZN
• Castrova asks that the size be 3000 x 3000 pixels
Nice to have
• I prefer that it have have 1 dominating color to help it stand out.
• This is what I mean:
• https://www.filebarnex.com/s/q4k8tmwpl2vbx9r/Castrova%20-%20one%20dominating%20color.png?dl=0
• I really like this color:
• https://www.filebarnex.com/s/k9v1wfzhr3ndy7c/color%20I%20like.png?dl=0

```html
<!DOCTYPE html>
<html lang="en">
<head>
<meta charset="UTF-8">
<title>Startup Stories – Podcast Cover</title>
<link href="https://fonts.googleapis.com/css2?family=Cinzel:wght@400;700&display=swap" rel="stylesheet">
<style>
  :root {
    --bg-green: #1f6a4b;
    --title-gold: #e6bd2f;
    --badge-gold: #f2c12e;
    --badge-ink: #2a2a26;
    --portrait-light: #b99b86;
    --portrait-dark: #4a4c52;
  }
  html, body {
    margin: 0;
    padding: 0;
    overflow: hidden;
    background: var(--bg-green);
  }
  .cover {
    position: relative;
    width: 1200px;
    height: 1200px;
    background: var(--bg-green);
    overflow: hidden;
  }
  .brand-badge {
    position: absolute;
    left: 65px;
    top: 79px;
    width: 309px;
    height: 91px;
    background: var(--badge-gold);
    display: flex;
    align-items: center;
    justify-content: center;
    z-index: 2;
  }
  .brand-name {
    font-family: "Cinzel", serif;
    font-weight: 700;
    font-size: 50px;
    letter-spacing: 1px;
    color: var(--badge-ink);
    line-height: 1;
  }
  .show-title {
    position: absolute;
    left: 58px;
    top: 362px;
    margin: 0;
    font-family: "Cinzel", serif;
    font-weight: 400;
    font-size: 108px;
    line-height: 122px;
    letter-spacing: 2px;
    color: var(--title-gold);
    z-index: 2;
  }
  .show-title span { display: block; }
  .host-portrait {
    position: absolute;
    inset: 0;
    width: 1200px;
    height: 1200px;
    z-index: 1;
  }
</style>
</head>
<body>
  <main class="cover">
    <div class="brand-badge">
      <span class="brand-name">TALVOREN</span>
    </div>

    <h1 class="show-title">
      <span>STARTUP</span>
      <span>STORIES</span>
    </h1>

    <svg class="host-portrait" viewBox="0 0 1200 1200" role="img"
         aria-label="Photo of the host in a grey t-shirt, hands pressed together over his mouth">
      <defs>
        <linearGradient id="portrait-tone" x1="0" y1="0" x2="0" y2="1">
          <stop offset="0" stop-color="var(--portrait-light)"/>
          <stop offset="0.45" stop-color="var(--portrait-light)"/>
          <stop offset="0.6" stop-color="var(--portrait-dark)"/>
          <stop offset="1" stop-color="var(--portrait-dark)"/>
        </linearGradient>
      </defs>
      <path fill="url(#portrait-tone)"
            d="M650 90 C 690 20, 900 10, 950 90
               C 985 160, 960 330, 930 420
               C 1010 470, 1110 520, 1200 560
               L 1200 1200 L 480 1200
               C 490 1050, 520 900, 560 780
               C 580 700, 610 640, 640 600
               C 640 500, 645 420, 660 380
               C 630 300, 620 170, 650 90 Z"/>
    </svg>
  </main>
</body>
</html>
```